Vr holdings enterprise pty ltd

2 sided card black and red with white
Very professional and elegant

Target Market(s)

Construction and Development

Industry/Entity Type

Construction and development

Contact Information for Business Card

One side black, one side red/or white business logo in top corner, email: morgan@vrholdingsgroup.example

Requirements
Should not have
• Blue

```html
<!DOCTYPE html>
<html lang="en">
<head>
<meta charset="utf-8">
<title>VR Holdings – Business Card</title>
<link rel="stylesheet" href="https://fonts.googleapis.com/css2?family=Montserrat:wght@500;700;800&family=Questrial&display=swap">
<style>
  :root {
    --ink: #0a0a0a;
    --red: #e63a1f;
    --paper: #ffffff;
    --stage: #d9d7d3;
    --ghost: #141414;
    --muted: #1c1c1c;
  }
  * { box-sizing: border-box; margin: 0; padding: 0; }
  html, body { width: 1200px; height: 908px; overflow: hidden; }
  body {
    background: var(--stage);
    font-family: "Questrial", "Century Gothic", sans-serif;
    display: flex;
    align-items: center;
    justify-content: center;
    gap: 40px;
  }
  .card {
    position: relative;
    width: 540px;
    height: 308px;
    overflow: hidden;
    box-shadow: 0 10px 30px rgba(0,0,0,.18);
  }

  /* Front: black */
  .card--front { background: var(--ink); }
  .card--front .ghost-name {
    position: absolute;
    left: -20px;
    bottom: -18px;
    font-family: "Montserrat", sans-serif;
    font-weight: 800;
    font-size: 88px;
    letter-spacing: 2px;
    color: var(--ghost);
    white-space: nowrap;
  }
  .wordmark {
    display: flex;
    align-items: center;
    gap: 8px;
    font-family: "Montserrat", sans-serif;
    font-weight: 800;
    letter-spacing: 2px;
    white-space: nowrap;
  }
  .wordmark__dot {
    width: 9px; height: 9px;
    border-radius: 50%;
    background: var(--red);
  }
  .card--front .wordmark {
    position: absolute;
    left: 50%; top: 50%;
    transform: translate(-50%, -50%);
    color: var(--paper);
    font-size: 40px;
  }

  /* Back: white with red field */
  .card--back { background: var(--paper); }
  .red-field { position: absolute; inset: 0; }
  .card--back .wordmark {
    position: absolute;
    left: 150px; top: 56px;
    color: var(--ink);
    font-size: 34px;
  }
  .person {
    position: absolute;
    left: 118px; top: 148px;
    display: flex;
    align-items: flex-end;
    gap: 10px;
  }
  .person__name {
    background: var(--paper);
    color: var(--red);
    font-family: "Montserrat", sans-serif;
    font-weight: 800;
    font-size: 24px;
    padding: 2px 14px;
    border-radius: 14px;
  }
  .person__role {
    font-size: 13px;
    color: var(--muted);
    letter-spacing: .5px;
    padding-bottom: 4px;
  }
  .contact {
    position: absolute;
    left: 250px; top: 200px;
    list-style: none;
    display: flex;
    flex-direction: column;
    gap: 6px;
    font-size: 13px;
    color: var(--muted);
  }
  .contact__item { display: flex; align-items: center; gap: 7px; }
  .contact__icon {
    width: 16px; height: 16px;
    border-radius: 50%;
    background: var(--red);
    border: 2px solid var(--paper);
    display: flex; align-items: center; justify-content: center;
    flex: none;
  }
  .contact__icon svg { width: 9px; height: 9px; }
</style>
</head>
<body>

  <section class="card card--front" aria-label="Card front">
    <div class="ghost-name" aria-hidden="true">VR HOLDINGS</div>
    <div class="wordmark">VR HOLDINGS<span class="wordmark__dot"></span></div>
  </section>

  <section class="card card--back" aria-label="Card back">
    <svg class="red-field" viewBox="0 0 540 308" preserveAspectRatio="none" aria-hidden="true">
      <polygon points="0,120 120,120 360,308 0,308" fill="#e63a1f"/>
    </svg>

    <div class="wordmark">VR HOLDINGS<span class="wordmark__dot"></span></div>

    <div class="person">
      <span class="person__name">JOHN DOE</span>
      <span class="person__role">MANGAER</span>
    </div>

    <ul class="contact">
      <li class="contact__item">
        <span class="contact__icon">
          <svg viewBox="0 0 10 10"><path d="M2 1 L4 1 L4.5 3 L3.4 3.8 Q4.2 5.8 6.2 6.6 L7 5.5 L9 6 L9 8 Q5 9 2.5 6 Q1 4 2 1Z" fill="#fff"/></svg>
        </span>
        111-222-333
      </li>
      <li class="contact__item">
        <span class="contact__icon">
          <svg viewBox="0 0 10 10"><rect x="1" y="2.5" width="8" height="5.5" fill="#fff"/><path d="M1 2.5 L5 5.5 L9 2.5" stroke="#e63a1f" stroke-width="1" fill="none"/></svg>
        </span>
        morgan@vrholdingsgroup.example
      </li>
      <li class="contact__item">
        <span class="contact__icon">
          <svg viewBox="0 0 10 10"><path d="M5 1 L9 5 L8 5 L8 9 L2 9 L2 5 L1 5Z" fill="#fff"/></svg>
        </span>
        your address,your city,box 88900
      </li>
    </ul>
  </section>

</body>
</html>
```